Junior Builders Coastline Gala Poster

To Create a Poster for the Junior Builders Coastline Gala 2013

Target Market(s)

Young Professional Engineers aged 18-35. Male and Female

Requirements
Must have
• All Details required for the ball. Black and white/silver theme. Some kind of engineering theme. Must have the following text:

Join us in celebrating the Annual Junior Builders of Coastline Region Gala with a night of dinner and entertainment.
Saturday July 13th, 2013
Time: 7pm Arrival
Venue: Corvane Lodge Hotel, Perth
Dress: Formal
The evening will include drinks, a three-course dinner, music and dancing.
Ticket price $139, on sale now! To purchase tickets go to:
(website to be announced)
Proceeds go to Makers Across Rivers
is is an 18+ event. Open to general public.
Nice to have
• Modern, Classy, Similar to previous years designs. Possibly Masquerade themed.
Should not have
• Fish, environmental theme, rural Australia theme (these have been done)

```html
<!DOCTYPE html>
<html lang="en">
<head>
<meta charset="utf-8">
<title>Junior Builders Coastline Gala</title>
<link rel="stylesheet" href="https://fonts.googleapis.com/css2?family=Josefin+Slab:wght@400;600;700&family=Raleway:wght@700;800&display=swap">
<style>
  :root {
    --night: #111111;
    --night-line: #1b1b1b;
    --silver: #ececec;
    --silver-dim: #cfcfcf;
    --accent: #e0291e;
    --paper: #ffffff;
    --ink: #111111;
  }
  * { box-sizing: border-box; margin: 0; padding: 0; }
  html, body { width: 846px; height: 1200px; overflow: hidden; background: var(--night); }
  .poster {
    position: relative;
    width: 846px;
    height: 1200px;
    overflow: hidden;
    background:
      repeating-linear-gradient(135deg, var(--night) 0 3px, var(--night-line) 3px 4px);
    color: var(--silver);
    font-family: "Josefin Slab", Georgia, serif;
    text-align: center;
  }
  .event-date {
    position: absolute;
    top: 20px; left: 0; right: 0;
    font-size: 50px;
    font-weight: 600;
    letter-spacing: 3px;
    text-transform: uppercase;
    color: var(--silver);
  }
  .event-date sup { font-size: 24px; vertical-align: 22px; }
  .masquerade-art {
    position: absolute;
    left: 38px; top: 78px;
    width: 752px; height: 520px;
    background:
      radial-gradient(ellipse 26% 48% at 31% 50%, #f2f2f2 0%, #cfcfcf 55%, rgba(17,17,17,0) 100%),
      radial-gradient(ellipse 24% 46% at 72% 53%, #f0f0f0 0%, #c9c9c9 55%, rgba(17,17,17,0) 100%),
      radial-gradient(circle at 35% 20%, rgba(224,80,60,0.35), rgba(0,0,0,0) 30%);
  }
  .organiser {
    position: absolute;
    top: 576px; left: 0; right: 0;
    display: flex; justify-content: center; align-items: center; gap: 10px;
    font-size: 15px; font-weight: 700; letter-spacing: 1px;
    text-transform: uppercase; color: var(--paper);
  }
  .organiser-mark { width: 30px; height: 30px; background: var(--accent); }
  .presenter {
    position: absolute;
    top: 648px; left: 0; right: 0;
    font-size: 25px; color: var(--accent);
  }
  .event-title {
    position: absolute;
    top: 690px; left: 0; right: 0;
    font-family: "Raleway", Arial, sans-serif;
    font-weight: 800;
    font-size: 58px;
    line-height: 60px;
    letter-spacing: 2px;
    text-transform: uppercase;
    color: var(--silver);
    text-shadow: 0 2px 0 #777;
  }
  .invitation {
    position: absolute;
    top: 868px; left: 20px; right: 20px;
    font-size: 24px; line-height: 32px;
    letter-spacing: 1px;
    text-transform: uppercase;
    color: var(--silver);
  }
  .details {
    position: absolute;
    top: 977px; left: 0; right: 0;
    font-size: 18px; line-height: 24px;
    color: var(--silver-dim);
  }
  .ticket-band {
    position: absolute;
    left: 0; right: 0; top: 1088px; bottom: 0;
    background: var(--paper);
    color: var(--ink);
    font-size: 19px; line-height: 34px;
    padding-top: 22px;
  }
  .ticket-band .link { color: var(--accent); }
</style>
</head>
<body>
  <main class="poster">
    <h2 class="event-date">Saturday July 13<sup>th</sup>, 2013</h2>
    <div class="masquerade-art" role="img" aria-label="Two white Venetian masquerade masks with silver swirl decoration, softly lit in red, on black"></div>
    <div class="organiser"><span class="organiser-mark"></span><span>Civic Builders Guild</span></div>
    <p class="presenter">Junior Builders of Coastline Region presents</p>
    <h1 class="event-title">The Young<br>Professionals Ball</h1>
    <p class="invitation">Join us in celebrating the annual Junior Builders of Coastline Region Gala with a night of dinner and entertainment.</p>
    <p class="details">The evening will include drinks, a three-course dinner, music and dancing.<br>Proceeds go to Makers Across Rivers<br>Is an 18+ event. Open to general public.</p>
    <footer class="ticket-band">
      <p>TIME: 7pm Arrival | VENUE: Corvane Lodge Hotel, Perth, | DRESS: Formal</p>
      <p>Ticket price: $139, on sale now! To purchase tickets go to: <span class="link">www.galanight.com.au</span></p>
    </footer>
  </main>
</body>
</html>
```